Harbor Kestrel
Your Trusted Advisors
Professional
Rosalind Okafor
Partner
418 Tamarack Lane
Larkmoor, PA 19388
rosalind.okafor@harborkestrel.co
www.harborkestrel.co

```html
<!DOCTYPE html>
<html lang="en">
<head>
<meta charset="utf-8">
<title>Harbor Kestrel Stationery</title>
<link href="https://fonts.googleapis.com/css2?family=Open+Sans:wght@400;600;700&display=swap" rel="stylesheet">
<style>
:root{
  --bg:#d8d5d0;
  --paper:#ffffff;
  --red:#c4161c;
  --red-dark:#8e0e12;
  --ink:#2b2b2b;
  --muted:#6d6d6d;
  --rule:#bdbdbd;
}
*{box-sizing:border-box;margin:0;padding:0}
html,body{width:1200px;height:559px;overflow:hidden}
body{background:var(--bg);font-family:"Open Sans",Arial,sans-serif;color:var(--ink);position:relative}
.sheet{position:absolute;background:var(--paper);overflow:hidden;box-shadow:0 2px 6px rgba(0,0,0,.25)}
.corner{position:absolute;right:0;bottom:0}
.brand{display:flex;align-items:center;gap:5px}
.brand-mark{width:12px;height:12px;background:var(--red);flex:none}
.brand-name{font-weight:700;color:var(--red);text-transform:uppercase;letter-spacing:.3px;white-space:nowrap}
.contact{position:absolute;font-size:5px;line-height:1.5;color:var(--muted);white-space:nowrap}

/* fax */
.fax{left:19px;top:24px;width:214px;height:492px}
.fax .brand{position:absolute;left:14px;top:22px}
.fax .brand-name{font-size:9px}
.fax .contact{left:124px;top:16px}
.fax-title{position:absolute;left:14px;top:104px;font-size:20px;font-weight:700;letter-spacing:1px}
.fax-fields{position:absolute;left:14px;top:148px;width:186px;display:grid;grid-template-columns:1fr 1fr;column-gap:12px;row-gap:18px}
.field{display:flex;align-items:flex-end;gap:4px;font-size:6px;font-weight:600}
.field span.line{flex:1;border-bottom:.6px solid var(--rule);height:7px}
.fax-checks{position:absolute;left:14px;top:280px;width:188px;display:flex;justify-content:space-between;font-size:4.4px;color:var(--muted)}
.fax-checks label{display:flex;align-items:center;gap:2px;white-space:nowrap}
.box{width:5px;height:5px;border:.6px solid var(--muted);display:inline-block}
.fax-rule{position:absolute;left:14px;top:292px;width:188px;border-top:.6px solid var(--rule)}

/* letterhead */
.letter{left:252px;top:24px;width:356px;height:492px}
.letter .brand{position:absolute;left:24px;top:26px}
.letter .brand-name{font-size:11px}
.letter .contact{left:258px;top:16px}
.letter-body{position:absolute;left:24px;top:116px;width:310px;font-size:5.6px;line-height:1.75;color:var(--muted)}
.letter-body p{margin-bottom:8px}
.sign{height:16px;width:60px;background:linear-gradient(90deg,#cfcfcf,#e6e6e6);margin:4px 0 4px}
.signer{color:var(--ink);font-weight:600}

/* envelope */
.envelope{left:629px;top:62px;width:554px;height:278px}
.env-band{position:absolute;left:0;top:0;width:100%;height:20px;background:var(--red)}
.envelope .brand{position:absolute;left:172px;top:132px}
.envelope .brand-mark{width:16px;height:16px}
.envelope .brand-name{font-size:15px}
.envelope .contact{left:172px;top:160px;font-size:5.5px}

/* cards */
.card{width:180px;height:150px;top:352px;border-radius:4px}
.card-back{left:810px}
.card-front{left:1000px}
.card .brand{position:absolute;left:50%;transform:translateX(-50%)}
.card .brand-name{font-size:10px}
.card-back .brand{top:26px}
.card-back .tagline{position:absolute;left:0;right:0;top:44px;text-align:center;font-size:5px;color:var(--muted)}
.person{position:absolute;left:40px;top:70px;font-size:5px;line-height:1.55;color:var(--muted)}
.person strong{display:block;font-size:7px;color:var(--ink)}
.card-front .brand{top:44px}
.card-front .tagline{position:absolute;left:0;right:0;top:64px;text-align:center;font-size:5.5px;color:var(--red);font-weight:600}
</style>
</head>
<body>

<section class="sheet fax">
  <div class="brand"><span class="brand-mark"></span><span class="brand-name">Harbor Kestrel</span></div>
  <div class="contact">418 Tamarack Lane<br>Larkmoor, PA 19388<br>(610) 555-0147<br>rosalind.okafor@harborkestrel.co<br>www.harborkestrel.co</div>
  <h1 class="fax-title">FAX</h1>
  <div class="fax-fields">
    <div class="field">To:<span class="line"></span></div><div class="field">From:<span class="line"></span></div>
    <div class="field">Fax:<span class="line"></span></div><div class="field">Pages:<span class="line"></span></div>
    <div class="field">Phone:<span class="line"></span></div><div class="field">Date:<span class="line"></span></div>
    <div class="field">Re:<span class="line"></span></div><div class="field">CC:<span class="line"></span></div>
  </div>
  <div class="fax-checks">
    <label><i class="box"></i>Urgent</label><label><i class="box"></i>For Review</label><label><i class="box"></i>Please Comment</label><label><i class="box"></i>Please Reply</label><label><i class="box"></i>Please Recycle</label>
  </div>
  <div class="fax-rule"></div>
  <svg class="corner" width="84" height="66" viewBox="0 0 84 66"><polygon points="84,0 84,66 36,66" fill="var(--red)"/><polygon points="84,28 84,66 62,66" fill="var(--red-dark)"/></svg>
</section>

<section class="sheet letter">
  <div class="brand"><span class="brand-mark"></span><span class="brand-name">Harbor Kestrel</span></div>
  <div class="contact">418 Tamarack Lane<br>Larkmoor, PA 19388<br>(610) 555-0147<br>rosalind.okafor@harborkestrel.co<br>www.harborkestrel.co</div>
  <div class="letter-body">
    <p>Dear Client,</p>
    <p>We are pleased to confirm our engagement and outline the next steps for your review. Our team will prepare the initial report and share findings within two weeks of our first meeting, with a clear summary of each option open to you.</p>
    <p>Please review the enclosed schedule and let us know of any changes. We value your trust and look forward to working closely with you on every stage of this project, from planning through to final delivery and follow-up.</p>
    <p>Our advisors will contact you to arrange a short call at a time that suits you. During that call we will agree on goals, timelines and the documents we need from your side to begin the work without delay.</p>
    <p>Should you have questions, our office is open weekdays and our advisors are always glad to help. Thank you for choosing us as your partner.</p>
    <p>Kind regards,</p>
    <div class="sign" role="img" aria-label="Handwritten signature"></div>
    <p class="signer">Rosalind Okafor<br>Partner</p>
  </div>
  <svg class="corner" width="104" height="78" viewBox="0 0 104 78"><polygon points="104,0 104,78 44,78" fill="var(--red)"/><polygon points="104,34 104,78 76,78" fill="var(--red-dark)"/></svg>
</section>

<section class="sheet envelope">
  <div class="env-band"></div>
  <div class="brand"><span class="brand-mark"></span><span class="brand-name">Harbor Kestrel</span></div>
  <div class="contact">418 Tamarack Lane<br>Larkmoor, PA 19388</div>
  <svg class="corner" width="120" height="108" viewBox="0 0 120 108"><polygon points="120,0 120,108 54,108" fill="var(--red)"/><polygon points="120,46 120,108 88,108" fill="var(--red-dark)"/></svg>
</section>

<section class="sheet card card-back">
  <div class="brand"><span class="brand-mark"></span><span class="brand-name">Harbor Kestrel</span></div>
  <div class="tagline">Professional</div>
  <div class="person"><strong>Rosalind Okafor</strong>Partner<br>(610) 555-0147<br>rosalind.okafor@harborkestrel.co<br>www.harborkestrel.co</div>
  <svg class="corner" width="56" height="48" viewBox="0 0 56 48"><polygon points="56,0 56,48 22,48" fill="var(--red)"/></svg>
</section>

<section class="sheet card card-front">
  <div class="brand"><span class="brand-mark"></span><span class="brand-name">Harbor Kestrel</span></div>
  <div class="tagline">Your Trusted Advisors</div>
  <svg class="corner" width="56" height="48" viewBox="0 0 56 48"><polygon points="56,0 56,48 22,48" fill="var(--red)"/></svg>
</section>

</body>
</html>
```